Emerging Australian photographer

I'm based in Cunderdin, a small rural town in the Wheatbelt area of Western Australia. So its a good thing that I love to travel further afield both for pleasure and for work. To me that is one and the same thing in any event!

My desire is to take photos that make the viewers heart skip. I love taking photos of people doing the things they love or being with the people they love. For me, the joy of photography comes with capturing the 'moments between the moments'. I like candid photography best of all - like when the new husband is staring joyfully at his bride and at that minute is unaware of the photographer capturing the moment.

I am available for weddings, engagements, birthdays, special events, newborns, family or individual portraits. By the end of the year I will be accredited with the Coastal Guild of Image Makers.

I need a card that stands out but is elegant and would sit well on the table at a wedding or be given out in the church grounds. Classy and a little bit sassy.

Target Market(s)

Consumers who are seeking photographic services, eg wedding guests who see me at work and make enquiries.

Industry/Entity Type

Church

Contact Information for Business Card

Delia Marchetti Photography
Delia Marchetti
0452 368 071
www.deliamarchetti.com.au
photos@deliamarchetti.com.au

Requirements
Must have
• Must fit with the theme in the watermarks, but be crisp and modern.
Nice to have
• However it's not essential to have the pink! Chatterbook and Peeper logos.
Should not have
• Old style fonts like times new roman.

```html
<!DOCTYPE html>
<html lang="en">
<head>
<meta charset="utf-8">
<title>Delia Marchetti Photography — Business Card</title>
<link rel="stylesheet" href="https://fonts.googleapis.com/css2?family=Questrial&display=swap">
<style>
  :root {
    --page: #ffffff;
    --card: #262626;
    --band: #343434;
    --band-edge: #3a3a3a;
    --ink: #ffffff;
    --ink-soft: #ececec;
    --accent: #f08cc0;
  }
  * { margin: 0; padding: 0; box-sizing: border-box; }
  html, body {
    width: 1200px;
    height: 2250px;
    overflow: hidden;
    background: var(--page);
    font-family: "Questrial", "Helvetica Neue", Arial, sans-serif;
  }
  .sheet { position: relative; width: 1200px; height: 2250px; }

  .card {
    position: absolute;
    width: 1158px;
    height: 713px;
    background: var(--card);
    overflow: hidden;
  }
  .card--contact { left: 21px; top: 12px; }
  .card--brand   { left: 21px; top: 741px; }

  .wordmark {
    position: absolute;
    left: 0; right: 0;
    display: flex;
    align-items: center;
    justify-content: center;
    gap: 18px;
    color: var(--ink);
    letter-spacing: 0.02em;
    white-space: nowrap;
  }
  .wordmark__dot {
    border-radius: 50%;
    background: var(--accent);
    flex: none;
  }
  .card--contact .wordmark { top: 220px; font-size: 44px; }
  .card--contact .wordmark__dot { width: 18px; height: 18px; }
  .card--brand .wordmark { top: 320px; font-size: 58px; }
  .card--brand .wordmark__dot { width: 22px; height: 22px; }

  .pattern-band {
    position: absolute;
    left: 0; right: 0;
    top: 358px;
    height: 194px;
    background: linear-gradient(90deg, var(--band), var(--band-edge) 50%, var(--band));
  }

  .contact {
    position: absolute;
    left: 0; right: 0;
    top: 392px;
    text-align: center;
    color: var(--ink-soft);
    font-size: 28px;
    line-height: 48px;
    letter-spacing: 0.02em;
  }
  .contact__name { color: var(--ink); font-size: 31px; }
  .contact__phone { color: var(--accent); font-size: 31px; margin-left: 10px; }

  .flat-set {
    position: absolute;
    left: 0; right: 0;
    top: 1540px;
    height: 600px;
  }
  .flat-set .card { transform-origin: 0 0; transform: scale(0.47); }
  .flat-set .card--brand   { left: 40px;  top: 60px; }
  .flat-set .card--contact { left: 616px; top: 180px; }
</style>
</head>
<body>
<main class="sheet">

  <section class="card card--contact" aria-label="Business card, contact side">
    <div class="wordmark"><span class="wordmark__dot"></span>Delia Marchetti Photography</div>
    <div class="pattern-band" role="img" aria-label="Band of soft grey decorative swirls"></div>
    <div class="contact">
      <p><span class="contact__name">Delia Marchetti</span><span class="contact__phone">0452 368 071</span></p>
      <p>www.deliamarchetti.com.au</p>
      <p>photos@deliamarchetti.com.au</p>
    </div>
  </section>

  <section class="card card--brand" aria-label="Business card, brand side">
    <div class="wordmark"><span class="wordmark__dot"></span>Delia Marchetti Photography</div>
  </section>

  <div class="flat-set" aria-label="Both card sides together">
    <section class="card card--brand">
      <div class="wordmark"><span class="wordmark__dot"></span>Delia Marchetti Photography</div>
    </section>
    <section class="card card--contact">
      <div class="wordmark"><span class="wordmark__dot"></span>Delia Marchetti Photography</div>
      <div class="pattern-band" role="img" aria-label="Band of soft grey decorative swirls"></div>
      <div class="contact">
        <p><span class="contact__name">Delia Marchetti</span><span class="contact__phone">0452 368 071</span></p>
        <p>www.deliamarchetti.com.au</p>
        <p>photos@deliamarchetti.com.au</p>
      </div>
    </section>
  </div>

</main>
</body>
</html>
```